International Trading Company, 'KIRO' needs a Business Card

The company name is "KIRO" and it has own logo design.
I'd like to use its logo on this business card.
I need two side Business Card.
I'll look forward to your great design.
Thank you very much in advance.

Contact Information for Business Card

Company Name : Kiro Harbour Limited
Information Example
Dorian Pallister
Mobile(use icon please) : 1 (212) 555-0143
Tel(use icon please) : 1 (212) 555-0178
Email(use icon please) : dorian27@kiroharbour-mail.com
Address(use icon please) : 482 Halden Ave, New York, NY 10160, USA

```html
<!DOCTYPE html>
<html lang="en">
<head>
<meta charset="utf-8">
<title>KIRO Business Card</title>
<link rel="stylesheet" href="https://fonts.googleapis.com/css2?family=Arimo:wght@400;700&display=swap">
<style>
  :root {
    --page-bg: #1c1c1c;
    --card-dark: #4a4a4a;
    --card-light: #f2f2f2;
    --ink-dark: #4a4a4a;
    --ink-light: #ececec;
    --ink-muted: #d4d4d4;
    --stripe: #4a4a4a;
    --icon-bg: #d9d9d9;
  }
  * { margin: 0; padding: 0; box-sizing: border-box; }
  html, body { width: 1200px; height: 997px; overflow: hidden; }
  body {
    background: var(--page-bg);
    font-family: "Arimo", Arial, sans-serif;
    position: relative;
  }
  .card {
    position: absolute;
    left: 220px;
    width: 760px;
    height: 434px;
    overflow: hidden;
  }
  .card-front { top: 50px; background: var(--card-dark); }
  .card-back { top: 513px; background: var(--card-dark); }

  .brand-name {
    font-family: "Arimo", Arial, sans-serif;
    font-weight: 700;
    letter-spacing: 4px;
    line-height: 1;
  }
  .card-front .brand-name {
    position: absolute;
    left: 0; right: 0; top: 150px;
    text-align: center;
    font-size: 140px;
    color: var(--ink-light);
  }

  .back-panel {
    position: absolute;
    left: 0; top: 0; bottom: 0;
    width: 372px;
    background: var(--card-light);
  }
  .back-stripes {
    position: absolute;
    left: 372px; top: 0; bottom: 0;
    width: 28px;
    background:
      linear-gradient(to right,
        var(--card-light) 0 4px,
        var(--stripe) 4px 9px,
        var(--card-light) 9px 16px,
        var(--stripe) 16px 21px,
        var(--card-light) 21px 26px,
        var(--card-dark) 26px 28px);
  }
  .back-panel .brand-name {
    position: absolute;
    left: 40px; top: 150px;
    font-size: 96px;
    color: var(--ink-dark);
  }
  .website {
    position: absolute;
    left: 40px; bottom: 56px;
    font-weight: 700;
    font-size: 17px;
    letter-spacing: 5px;
    color: var(--ink-dark);
  }

  .person {
    position: absolute;
    left: 430px; top: 70px;
    color: var(--ink-light);
    text-align: center;
  }
  .person-name {
    font-weight: 700;
    font-size: 21px;
    letter-spacing: 1px;
    text-transform: uppercase;
  }
  .person-title {
    font-weight: 700;
    font-size: 15px;
    margin-top: 4px;
    color: var(--ink-muted);
  }
  .contact-list {
    position: absolute;
    left: 424px; right: 16px; bottom: 44px;
    list-style: none;
    color: var(--ink-light);
    font-size: 15px;
  }
  .contact-item {
    display: flex;
    align-items: center;
    gap: 8px;
    margin-top: 9px;
    white-space: nowrap;
  }
  .contact-icon { width: 18px; height: 18px; flex: none; }
</style>
</head>
<body>

<section class="card card-front" aria-label="Business card front">
  <div class="brand-name">KIRO</div>
</section>

<section class="card card-back" aria-label="Business card back">
  <div class="back-panel">
    <div class="brand-name">KIRO</div>
    <div class="website">www.kiroharbour.com</div>
  </div>
  <div class="back-stripes"></div>

  <div class="person">
    <div class="person-name">Dorian Pallister</div>
    <div class="person-title">Director</div>
  </div>

  <ul class="contact-list">
    <li class="contact-item">
      <svg class="contact-icon" viewBox="0 0 18 18" aria-hidden="true">
        <circle cx="9" cy="9" r="9" fill="var(--icon-bg)"/>
        <rect x="6" y="3.5" width="6" height="11" rx="1.2" fill="none" stroke="#4a4a4a" stroke-width="1.3"/>
        <circle cx="9" cy="12.4" r="0.8" fill="#4a4a4a"/>
      </svg>
      <span>1 (212) 555-0143</span>
    </li>
    <li class="contact-item">
      <svg class="contact-icon" viewBox="0 0 18 18" aria-hidden="true">
        <circle cx="9" cy="9" r="9" fill="var(--icon-bg)"/>
        <path d="M4.5 7.5 Q9 4 13.5 7.5 L12.5 9 L11 8.3 L11 7.4 Q9 6.8 7 7.4 L7 8.3 L5.5 9 Z M6 9.5 H12 V13 H6 Z" fill="#4a4a4a"/>
      </svg>
      <span>1 (212) 555-0178</span>
    </li>
    <li class="contact-item">
      <svg class="contact-icon" viewBox="0 0 18 18" aria-hidden="true">
        <circle cx="9" cy="9" r="9" fill="var(--icon-bg)"/>
        <rect x="4.5" y="6" width="9" height="6.5" fill="none" stroke="#4a4a4a" stroke-width="1.2"/>
        <path d="M4.5 6 L9 9.6 L13.5 6" fill="none" stroke="#4a4a4a" stroke-width="1.2"/>
      </svg>
      <span>dorian27@kiroharbour-mail.com</span>
    </li>
    <li class="contact-item">
      <svg class="contact-icon" viewBox="0 0 18 18" aria-hidden="true">
        <circle cx="9" cy="9" r="9" fill="var(--icon-bg)"/>
        <path d="M9 3.5 A3.6 3.6 0 0 1 12.6 7.1 C12.6 9.8 9 14.5 9 14.5 C9 14.5 5.4 9.8 5.4 7.1 A3.6 3.6 0 0 1 9 3.5 Z" fill="#4a4a4a"/>
        <circle cx="9" cy="7.1" r="1.4" fill="var(--icon-bg)"/>
      </svg>
      <span>482 Halden Ave, New York, NY 10160, USA</span>
    </li>
  </ul>
</section>

</body>
</html>
```